Q.B.Y 'Qafilat Bin Yusr' for General Transportation

this company is a Iraqi based company.
It provides a number of logistics activities such as;
Overland Transportation
High and heavy logistics
Customs clearance
warehousing
Automotive logistics
The company has been registered since 2009.
If you have any other questions please feel free to ask.
Target Market(s)
Automotive
White goods
All Trading sectors
Industry/Entity Type
Automotive

```html
<!DOCTYPE html>
<html lang="en">
<head>
<meta charset="utf-8">
<title>Qafilat Bin Yusr Transportation</title>
<link href="https://fonts.googleapis.com/css2?family=Open+Sans:wght@300;400;600&family=Ubuntu:wght@400;500&display=swap" rel="stylesheet">
<style>
:root{
  --navy:#0b2a5c;
  --navy-dark:#081f47;
  --blue:#1a4f8a;
  --orange:#f0a318;
  --text:#666;
  --muted:#888;
  --line:#dcdcdc;
  --lime:#b7e31a;
  --page:#fff;
}
*{margin:0;padding:0;box-sizing:border-box}
html,body{width:1115px;height:1200px;overflow:hidden;background:var(--page)}
body{position:relative;font-family:"Open Sans",sans-serif;color:var(--text)}
.brand{position:absolute;left:94px;top:25px;display:flex;align-items:center;gap:12px}
.brand-mark{display:flex;align-items:center;gap:8px}
.brand-square{width:22px;height:22px;background:var(--navy)}
.brand-name{font-family:"Ubuntu",sans-serif;font-weight:500;font-size:46px;color:var(--navy);letter-spacing:1px;line-height:59px}
.brand-text{font-family:"Ubuntu",sans-serif;font-size:15px;line-height:17px;color:var(--navy)}
.brand-text .sub{color:#888}
.brand-text .web{font-size:11px;letter-spacing:.5px;color:var(--navy)}
.lang{position:absolute;left:752px;top:58px;width:100px;height:30px;border:1px solid #ccc;border-radius:2px;font-size:13px;color:#333;display:flex;align-items:center;padding-left:10px;gap:8px;background:linear-gradient(#fff,#f2f2f2)}
.lang .flag{width:18px;height:12px;background:#2a3f8f}
.lang .caret{margin-left:auto;margin-right:8px;width:0;height:0;border-left:5px solid transparent;border-right:5px solid transparent;border-top:6px solid #555}
.call{position:absolute;right:101px;top:38px;text-align:right;white-space:nowrap}
.call .label{font-size:19px;font-weight:300;color:#999;line-height:26px}
.call .phone{font-size:22px;color:var(--blue);line-height:30px;letter-spacing:.2px}
.nav{position:absolute;left:92px;top:105px;width:945px;height:45px;display:flex;background:linear-gradient(var(--blue),var(--navy-dark))}
.nav a{display:flex;align-items:center;justify-content:center;color:#fff;text-decoration:none;font-size:15px;letter-spacing:.3px;border-right:1px solid #062050;border-left:1px solid #2a5d96}
.nav a:first-child{border-left:0}.nav a:last-child{border-right:0}
.hero{position:absolute;left:92px;top:150px;width:945px;height:382px;background:linear-gradient(180deg,#a07a5e 0%,#b9b0a0 45%,#c8c2b6 70%,#9c8d77 100%);border:1px solid #ddd}
.hero-band{position:absolute;left:0;top:189px;width:478px;height:105px;background:var(--orange);clip-path:polygon(0 0,440px 0,478px 52px,440px 105px,0 105px);padding:18px 0 0 22px;color:#fff}
.hero-band h1{font-family:"Ubuntu",sans-serif;font-weight:400;font-size:30px;line-height:36px}
.hero-band p{font-weight:300;font-size:20px;margin-top:2px}
.dots{position:absolute;left:440px;top:350px;display:flex;gap:4px}
.dots span{width:14px;height:14px;border-radius:50%;background:#fff}
.dots span:first-child{background:var(--lime)}
.services{position:absolute;left:92px;top:552px;width:945px;height:239px;border:1px solid var(--line);border-radius:3px;background:linear-gradient(#fff 70%,#f1f1f1)}
.card{position:absolute;top:20px;width:214px}
.card .photo{width:214px;height:105px;border:1px solid #ccc}
.card h3{font-family:"Ubuntu",sans-serif;font-weight:400;font-size:19px;color:var(--blue);margin-top:8px;white-space:nowrap}
.card p{font-size:11.5px;line-height:17px;color:var(--muted);margin-top:3px}
.card a{display:inline-block;margin-top:6px;font-size:12.5px;font-weight:600;color:var(--blue);text-decoration:none}
.welcome{position:absolute;left:95px;top:824px;width:640px}
.welcome h2{font-weight:300;font-size:28px;color:#444}
.welcome h4{font-weight:300;font-size:17px;color:#555;margin-top:4px}
.welcome p{font-weight:300;font-size:12px;line-height:22px;color:#777;margin-top:6px}
.welcome p+p{margin-top:10px}
.side{position:absolute;left:772px;top:830px;width:232px}
.side h2{font-family:"Ubuntu",sans-serif;font-weight:400;font-size:24px;color:var(--blue);margin-left:4px;white-space:nowrap}
.side ul{list-style:none;margin-top:8px}
.side li{font-size:12px;color:#555;height:28px;line-height:28px;border-bottom:1px solid var(--line);padding-left:20px;position:relative;white-space:nowrap}
.side li:last-child{border-bottom:0}
.side li::before{content:"";position:absolute;left:8px;top:10px;border-top:4px solid transparent;border-bottom:4px solid transparent;border-left:4px solid var(--blue)}
.footer{position:absolute;left:0;top:1102px;width:1115px;height:98px;background:var(--navy)}
.footer nav{position:absolute;left:98px;top:24px;font-size:14.5px;color:#fff;white-space:nowrap}
.footer nav span{margin:0 8px;color:#c9d3e4}
.footer .copy{position:absolute;left:100px;top:56px;font-size:13px;color:#dfe6f1}
.social{position:absolute;left:917px;top:29px;display:flex;gap:7px}
.social span{width:22px;height:22px;border-radius:3px;background:#5b7fb3}
</style>
</head>
<body>
<header>
  <div class="brand">
    <div class="brand-mark"><div class="brand-square"></div><span class="brand-name">Q.B.Y</span></div>
    <div class="brand-text">Qafilat Bin Yusr<br><span class="sub">Transportation</span><br><span class="web">www.qbytrans.com</span></div>
  </div>
  <div class="lang"><span class="flag"></span>English<span class="caret"></span></div>
  <div class="call"><div class="label">Call Us Now</div><div class="phone">620.555.0142</div></div>
</header>
<nav class="nav">
  <a style="width:91px">HOME</a><a style="width:116px">ABOUT US</a><a style="width:107px">SERVICES</a><a style="width:152px">WAREHOUSING</a><a style="width:111px">PROJECTS</a><a style="width:149px">TESTIMONIALS</a><a style="width:106px">SUPPORT</a><a style="width:113px">CONTACT</a>
</nav>
<section class="hero" role="img" aria-label="Warehouse interior with stacked pallet racks and a yellow forklift">
  <div class="hero-band"><h1>Transportation Service Provider</h1><p>Lorem ipsum dolor sit amet consectetuer</p></div>
  <div class="dots"><span></span><span></span><span></span><span></span></div>
</section>
<section class="services">
  <div class="card" style="left:23px"><div class="photo" role="img" aria-label="Blue truck with container on a highway" style="background:linear-gradient(#9cc3e4,#7fa36a 60%,#8a8a8a)"></div><h3>Overland Transportation</h3><p>Morbi eget arcu Morbi porta libero id ullamcorper nonummy nibh ligula</p><a>Read More ›</a></div>
  <div class="card" style="left:254px"><div class="photo" role="img" aria-label="Heavy freight truck trailer" style="background:linear-gradient(#b7b09a,#8d8466 60%,#5e5a4a)"></div><h3>High and Heavy logistics</h3><p>Morbi eget arcu Morbi porta libero id ullamcorper nonummy nibh ligula</p><a>Read More ›</a></div>
  <div class="card" style="left:484px"><div class="photo" role="img" aria-label="Customs officers inspecting cargo boxes" style="background:linear-gradient(#c8d0d8,#6d7680 55%,#b59a7c)"></div><h3>Customs Clearance</h3><p>Morbi eget arcu Morbi porta libero id ullamcorper nonummy nibh ligula</p><a>Read More ›</a></div>
  <div class="card" style="left:715px"><div class="photo" role="img" aria-label="Warehouse workers moving wrapped pallets" style="background:linear-gradient(#9aa0ab,#6d7380 55%,#b9413a)"></div><h3>Warehousing</h3><p>Morbi eget arcu Morbi porta libero id ullamcorper nonummy nibh ligula</p><a>Read More ›</a></div>
</section>
<section class="welcome">
  <h2>Welcome to Our Website Mainpage..</h2>
  <h4>Proin nulla arcu nonummy luctus dictum eget fermentum et lorem</h4>
  <p>Duis tincidunt lectus quis dui viverra vestibulum. Suspendisse vulputate aliquam dui. Nulla elementum dui ut augue. Aliquam vehicula mi at mauris. Maecenas placerat, nisl at consequat rhoncus, sem nunc gravida justo, quis eleifend arcu velit quis lacus. Morbi magna magna, tincidunt a, mattis non, imperdiet vitae, tellus. Sed odio est, auctor ac, sollicitudin in, consequat vitae, orci.</p>
  <p>Donec scelerisque leo ac risus. Praesent sit amet est. In dictum, dolor eu dictum porttitor, enim felis viverra mi, eget luctus massa purus quis odio. Etiam nulla massa, pharetra facilisis, volutpat in</p>
</section>
<aside class="side">
  <h2>Services Provides</h2>
  <ul>
    <li>Vivamus porttitor nisi eleifend</li>
    <li>Libero tempus libero lectus feugiat</li>
    <li>Morbi diam mauris viverra</li>
    <li>Morbi eget arcu</li>
    <li>Morbi porta libero id ullamcorper</li>
    <li>Ligula pulvinar metus eget</li>
  </ul>
</aside>
<footer class="footer">
  <nav>Home<span>|</span>About Us<span>|</span>Services<span>|</span>Warehousing<span>|</span>Projects<span>|</span>Testimonials<span>|</span>Support<span>|</span>Contact</nav>
  <div class="copy">Copyright © 2013 Company Name.&nbsp; All right reserved</div>
  <div class="social"><span></span><span></span><span></span><span></span></div>
</footer>
</body>
</html>
```